Caribbean pest control company needs a brochure design

We a full service, family owned pest control company based in the Bahamas and have just opened a second location. We would like a brochure that highlights our company and the services we provide. This brochure will be used as material to tell people who are not familiar with us, more about the company in general. We would like the final design to incorporate our company colors of navy blue and yellow (as depicted in the logo). Included in the uploaded files is the content for the brochure, as well as pictures. Several logo formats have been included for you to choose from. Pictures can be chosen as you see fit, and not all has to be included in the brochure. Stock photos of insects can also be used if desired. Feel free to be creative. Brochure can be either half fold or trifold. But half fold is preferable.

Target Market(s)

Anyone over 25. People who are concerned with pests in their living environment and business owners

Requirements
Must have
• Must include logo

```html
<!DOCTYPE html>
<html lang="en">
<head>
<meta charset="utf-8">
<title>Harbourline Pest Control – Brochure Cover</title>
<link rel="stylesheet" href="https://fonts.googleapis.com/css2?family=Montserrat:wght@600;800&display=swap">
<style>
  :root {
    --navy: #1f56a8;
    --navy-deep: #163f82;
    --yellow: #ecea4a;
    --yellow-light: #f6f49a;
    --yellow-pale: #fbfacc;
    --gold: #d9b740;
    --paper: #ffffff;
    --backdrop: #e4e4e4;
  }
  * { box-sizing: border-box; margin: 0; padding: 0; }
  html, body { width: 1200px; height: 790px; overflow: hidden; }
  body {
    background: var(--backdrop);
    font-family: "Montserrat", Arial, sans-serif;
    position: relative;
  }
  .cover {
    position: absolute;
    left: 330px; top: 35px;
    width: 540px; height: 720px;
    background: var(--paper);
    overflow: hidden;
    box-shadow: 0 6px 18px rgba(0,0,0,0.18);
  }
  .cover-art { position: absolute; inset: 0; }
  .brand {
    position: absolute;
    left: 44px; top: 86px;
    display: flex; align-items: center; gap: 12px;
  }
  .brand-dot {
    width: 22px; height: 22px; border-radius: 50%;
    background: var(--navy);
  }
  .brand-name {
    color: var(--navy);
    font-weight: 800;
    font-size: 30px;
    line-height: 1.05;
    letter-spacing: 0.5px;
  }
  .brand-name span { display: block; font-size: 17px; letter-spacing: 1px; }
  .tagline {
    position: absolute;
    left: 60px; top: 560px;
    width: 420px; height: 110px;
    color: var(--navy);
    text-align: center;
  }
  .tagline-frame {
    position: absolute; inset: 14px 0 0 0;
    border: 3px solid var(--navy);
  }
  .tagline-lead {
    position: absolute; left: 0; right: 0; top: 0;
    font-weight: 600; font-size: 18px; letter-spacing: 1px;
  }
  .tagline-lead b {
    background: var(--paper); padding: 0 10px; font-weight: 600;
  }
  .tagline-word {
    position: absolute; left: 0; right: 0;
    font-weight: 800; font-size: 38px; letter-spacing: 1px;
  }
  .tagline-word.first { top: 28px; }
  .tagline-word.second { top: 66px; }
</style>
</head>
<body>
  <section class="cover">
    <svg class="cover-art" width="540" height="720" viewBox="0 0 540 720" aria-hidden="false">
      <defs>
        <linearGradient id="yellowWash" x1="0" y1="0" x2="1" y2="1">
          <stop offset="0" stop-color="var(--yellow)"/>
          <stop offset="0.55" stop-color="var(--yellow-light)"/>
          <stop offset="1" stop-color="var(--yellow)"/>
        </linearGradient>
        <linearGradient id="gardenTones" x1="0" y1="0" x2="0" y2="1">
          <stop offset="0" stop-color="#5e8a4a"/>
          <stop offset="1" stop-color="#7fb04f"/>
        </linearGradient>
        <linearGradient id="indoorTones" x1="0" y1="0" x2="1" y2="1">
          <stop offset="0" stop-color="#d9cbbd"/>
          <stop offset="0.6" stop-color="#b89a7c"/>
          <stop offset="1" stop-color="#6a5a50"/>
        </linearGradient>
      </defs>
      <!-- yellow upper field with curved lower edge -->
      <path d="M0 0 H540 V390 C460 470 300 520 0 560 Z" fill="url(#yellowWash)"/>
      <path d="M0 565 C300 525 460 475 540 395" fill="none" stroke="var(--gold)" stroke-width="4"/>
      <circle cx="420" cy="40" r="210" fill="var(--yellow-pale)" opacity="0.35"/>
      <circle cx="160" cy="300" r="240" fill="var(--yellow)" opacity="0.35"/>
      <!-- orbit lines -->
      <path d="M250 210 C150 280 140 420 230 500" fill="none" stroke="var(--navy)" stroke-width="1.5"/>
      <path d="M200 240 C130 330 160 470 300 540" fill="none" stroke="#ffffff" stroke-width="1.5"/>
      <path d="M240 250 C170 320 180 430 290 500" fill="none" stroke="#ffffff" stroke-width="1"/>
      <circle cx="250" cy="210" r="5" fill="var(--navy)"/>
      <circle cx="200" cy="240" r="11" fill="#ffffff"/>
      <circle cx="240" cy="250" r="5" fill="#ffffff"/>
      <circle cx="230" cy="500" r="7" fill="var(--navy)"/>
      <circle cx="290" cy="500" r="4" fill="#ffffff"/>
      <circle cx="300" cy="540" r="22" fill="#ffffff"/>
      <!-- photo frames -->
      <circle cx="440" cy="170" r="90" fill="var(--gold)"/>
      <circle cx="440" cy="170" r="83" fill="url(#gardenTones)" role="img" aria-label="Photo: technician spraying a garden lawn"/>
      <circle cx="330" cy="360" r="150" fill="var(--gold)"/>
      <circle cx="330" cy="360" r="142" fill="url(#indoorTones)" role="img" aria-label="Photo: technician treating a kitchen cabinet indoors"/>
    </svg>

    <div class="brand">
      <div class="brand-dot"></div>
      <div class="brand-name">HARBOURLINE<span>PEST CONTROL</span></div>
    </div>

    <div class="tagline">
      <div class="tagline-frame"></div>
      <div class="tagline-lead"><b>ALWAYS</b></div>
      <div class="tagline-word first">PROFESSIONAL</div>
      <div class="tagline-word second">REASONABLE</div>
    </div>
  </section>
</body>
</html>
```